Postcard Design

We are Professional, quick and efficient. We are State Licensed and Insured. Gas•Water•Sewer Specializing in all of the customers plumbing needs. We accept credit cards. The law in Louisiana is that I have company address, and license number on all advertising. License number is LMP 4192. Address is 20517 north cedar ave. Cut Off, La. 70862

```html
<!DOCTYPE html>
<html lang="en">
<head>
<meta charset="utf-8">
<title>Delcambre Plumbing Postcard</title>
<link rel="stylesheet" href="https://fonts.googleapis.com/css2?family=Source+Sans+3:wght@400;600;700&family=Open+Sans:wght@800&family=Roboto+Condensed:wght@700&family=Roboto:wght@400;700&display=swap">
<style>
  :root{
    --bg:#e9eaec;
    --paper:#f2f2f2;
    --white:#ffffff;
    --ink:#111111;
    --blue:#2a72b8;
    --navy:#1d4f8a;
    --sky:#5bb8e6;
    --sky-pale:#8fcdf0;
    --grey-text:#555a60;
    --line:#8a8f95;
  }
  *{margin:0;padding:0;box-sizing:border-box}
  html,body{width:1029px;height:1200px;overflow:hidden;background:var(--bg)}
  .canvas{position:relative;width:1029px;height:1200px}
  .card{position:absolute;height:502px;overflow:hidden;box-shadow:0 2px 6px rgba(0,0,0,.25)}
  .card--front{left:87px;top:60px;width:776px;background:var(--paper)}
  .card--back{left:160px;top:612px;width:771px;background:var(--white)}
  .card__art{position:absolute;inset:0}
  .abs{position:absolute;white-space:nowrap}
  .company-name{font-family:"Source Sans 3",sans-serif;font-weight:600;text-transform:uppercase;letter-spacing:3px;line-height:1}
  .license{font-family:"Source Sans 3",sans-serif;font-weight:400;line-height:1}
  .services{font-family:"Open Sans",sans-serif;font-weight:800;line-height:50px;letter-spacing:1px}
  .tagline{font-family:"Source Sans 3",sans-serif;font-size:20px;line-height:19px;color:var(--ink)}
  .checks{list-style:none;font-family:"Source Sans 3",sans-serif;font-size:19px;color:var(--ink)}
  .checks li{display:flex;align-items:center;gap:14px;height:29px}
  .cta{font-family:"Roboto",sans-serif;font-weight:400}
  .phone{font-family:"Roboto",sans-serif;font-weight:700;display:flex;align-items:center;gap:6px}
  .condensed{font-family:"Roboto Condensed",sans-serif;font-weight:700;font-size:20px;line-height:24px;color:var(--white)}
  .return{font-family:"Source Sans 3",sans-serif;font-size:15px;line-height:20px;color:var(--grey-text)}
  .return__name{color:var(--blue);font-size:17px;font-weight:400;margin-bottom:12px}
  .stamp{position:absolute;left:655px;top:23px;width:94px;height:75px;border:1.5px solid var(--line)}
  .addr-line{position:absolute;left:487px;width:261px;border-top:1.5px solid var(--line)}
</style>
</head>
<body>
<main class="canvas">

  <section class="card card--front">
    <svg class="card__art" width="776" height="502" viewBox="0 0 776 502">
      <defs>
        <linearGradient id="photoTone" x1="0" y1="0" x2="1" y2="1">
          <stop offset="0" stop-color="#e6e8ec"/>
          <stop offset=".55" stop-color="#5c82b8"/>
          <stop offset="1" stop-color="#2f4f7d"/>
        </linearGradient>
        <linearGradient id="frontBand" x1="0" y1="0" x2="1" y2="0">
          <stop offset="0" stop-color="#17497f"/>
          <stop offset="1" stop-color="#2b78bd"/>
        </linearGradient>
        <radialGradient id="faucetTone" cx=".4" cy=".4" r=".7">
          <stop offset="0" stop-color="#f4f4f4"/>
          <stop offset="1" stop-color="#8c9096"/>
        </radialGradient>
      </defs>
      <path d="M418 0 C 368 80 345 200 368 320 C 378 360 395 385 420 400 L776 380 L776 0 Z" fill="var(--sky)"/>
      <path role="img" aria-label="Photo of a plumber in a blue cap and shirt working on pipes under a sink" d="M432 0 C 384 80 362 200 384 320 C 393 355 408 378 430 392 L776 372 L776 0 Z" fill="url(#photoTone)"/>
      <path d="M0 490 C 150 430 400 380 776 366 L776 378 C 400 392 150 442 0 502 Z" fill="var(--sky)"/>
      <path d="M0 502 C 150 442 400 392 776 378 L776 502 Z" fill="url(#frontBand)"/>
      <circle role="img" aria-label="Photo of a chrome faucet over a white sink" cx="357" cy="344" r="62" fill="url(#faucetTone)" stroke="#3a7fc0" stroke-width="3"/>
    </svg>

    <h1 class="abs company-name" style="left:20px;top:40px;font-size:29px;color:var(--ink)">Delcambre Plumbing</h1>
    <p class="abs license" style="left:40px;top:78px;font-size:18px;color:var(--ink)">LICENSED AND INSURED <span style="color:var(--blue)">LMP 4192</span></p>
    <h2 class="abs services" style="left:25px;top:124px;font-size:47px;color:var(--blue)">GAS<br>WATER<br>SEWER</h2>
    <p class="abs tagline" style="left:24px;top:284px">Specializing in all of the<br>customers plumbing needs!</p>
    <ul class="abs checks" style="left:28px;top:340px">
      <li><svg width="22" height="20" viewBox="0 0 22 20"><rect x="1" y="3" width="16" height="16" rx="3" fill="none" stroke="var(--blue)" stroke-width="2"/><path d="M5 10 L9 14 L20 2" fill="none" stroke="var(--blue)" stroke-width="2.4"/></svg>PROFESSIONAL</li>
      <li><svg width="22" height="20" viewBox="0 0 22 20"><rect x="1" y="3" width="16" height="16" rx="3" fill="none" stroke="var(--blue)" stroke-width="2"/><path d="M5 10 L9 14 L20 2" fill="none" stroke="var(--blue)" stroke-width="2.4"/></svg>QUICK</li>
      <li><svg width="22" height="20" viewBox="0 0 22 20"><rect x="1" y="3" width="16" height="16" rx="3" fill="none" stroke="var(--blue)" stroke-width="2"/><path d="M5 10 L9 14 L20 2" fill="none" stroke="var(--blue)" stroke-width="2.4"/></svg>EFFICIENT</li>
    </ul>
    <p class="abs cta" style="left:369px;top:412px;font-size:23px;color:var(--white)">Call today for your FREE QUOTE</p>
    <p class="abs phone" style="left:396px;top:448px;font-size:33px;color:var(--white)">
      <svg width="34" height="34" viewBox="0 0 34 34"><circle cx="17" cy="17" r="15" fill="none" stroke="var(--white)" stroke-width="2.5"/><path d="M11 9 C 9 11 9 14 11 17 C 13 21 16 24 20 25 C 22 26 24 25 25 23 L22 20 L19.5 21.5 C 17 20 14.5 17.5 13 15 L14.5 12.5 Z" fill="var(--white)"/></svg>1 985-555-0147
    </p>
  </section>

  <section class="card card--back">
    <svg class="card__art" width="771" height="502" viewBox="0 0 771 502">
      <defs>
        <linearGradient id="panelTone" x1="0" y1="0" x2="1" y2="1">
          <stop offset="0" stop-color="#1a5592"/>
          <stop offset="1" stop-color="#2f7fc4"/>
        </linearGradient>
        <linearGradient id="backBand" x1="0" y1="0" x2="1" y2="0">
          <stop offset="0" stop-color="#1a5a9a"/>
          <stop offset=".45" stop-color="#4aaee0"/>
          <stop offset="1" stop-color="#5cc2ec"/>
        </linearGradient>
      </defs>
      <path d="M0 0 H412 C 478 90 492 250 458 380 L440 460 L0 480 Z" fill="var(--sky-pale)"/>
      <path d="M0 0 H395 C 458 90 472 250 440 380 L422 460 L0 480 Z" fill="url(#panelTone)"/>
      <path d="M0 498 C 200 452 450 430 771 426" fill="none" stroke="#c6c8cb" stroke-width="6"/>
      <path d="M0 502 L0 501 C 200 458 450 436 771 432 L771 502 Z" fill="url(#backBand)"/>
      <circle role="img" aria-label="Photo of a plumber working under a bathroom sink" cx="83" cy="364" r="54" fill="#8a8f96" stroke="var(--white)" stroke-width="3"/>
      <circle role="img" aria-label="Photo of a wall-mounted tankless water heater" cx="204" cy="364" r="54" fill="#b9b6b1" stroke="var(--white)" stroke-width="3"/>
      <circle role="img" aria-label="Photo of new plumbing lines in a framed wall" cx="324" cy="364" r="54" fill="#a4794f" stroke="var(--white)" stroke-width="3"/>
    </svg>

    <h2 class="abs company-name" style="left:29px;top:36px;font-size:29px;color:#e6e8ea">Delcambre Plumbing</h2>
    <p class="abs license" style="left:53px;top:74px;font-size:18px;color:#d5d9de">LICENSED AND INSURED LMP 4192</p>
    <h3 class="abs services" style="left:29px;top:126px;font-size:40px;line-height:42px;color:var(--sky-pale)">REPAIR<br>REPLACEMENT<br>INSTALLATION</h3>
    <p class="abs condensed" style="left:29px;top:254px">YOUR SOURCE FOR COMPLETE<br>PLUMBING SOLUTIONS</p>

    <div class="abs return" style="left:462px;top:22px">
      <p class="return__name">Delcambre Plumbing</p>
      <p>20517 north cedar ave.</p>
      <p>Cut Off,&nbsp; La. 70862</p>
    </div>
    <div class="stamp"></div>
    <div class="addr-line" style="top:222px"></div>
    <div class="addr-line" style="top:256px"></div>
    <div class="addr-line" style="top:290px"></div>
    <div class="addr-line" style="top:324px"></div>

    <p class="abs cta" style="left:193px;top:464px;font-size:22px;color:var(--navy)">Call today for your FREE QUOTE</p>
    <p class="abs phone" style="left:507px;top:455px;font-size:30px;color:var(--navy)">
      <svg width="30" height="30" viewBox="0 0 34 34"><circle cx="17" cy="17" r="15" fill="none" stroke="var(--navy)" stroke-width="2.5"/><path d="M11 9 C 9 11 9 14 11 17 C 13 21 16 24 20 25 C 22 26 24 25 25 23 L22 20 L19.5 21.5 C 17 20 14.5 17.5 13 15 L14.5 12.5 Z" fill="var(--navy)"/></svg>1 985-555-0147
    </p>
  </section>

</main>
</body>
</html>
```